BrambleWorks business card

Looking for business card design that supports our company/software values. We have 2 logo designs at the moment but open to change if you think you can enhance the brand. Check out website www.brambleworks.com.au.

Target Market(s)

Education

Contact Information for Business Card

Name, title, mobile, email and website

Font styles to use
Sans Serif

Colors

Designer to choose colors to be used in the design.

Requirements
Must have
• BrambleWorks logo with tree and tagline on rear side with dark grey background colour

```html
<!DOCTYPE html>
<html lang="en">
<head>
<meta charset="utf-8">
<title>BrambleWorks Business Card</title>
<link href="https://fonts.googleapis.com/css2?family=Ubuntu:wght@400&family=Arimo:wght@400&display=swap" rel="stylesheet">
<style>
  :root {
    --backdrop: #e4e4e4;
    --card-dark: #1f2327;
    --card-dark-soft: #2c3035;
    --card-light: #f4f4f4;
    --curve-edge: #55575a;
    --accent: #f0a500;
    --leaf: #4f8f2a;
    --wordmark: #55595e;
    --ink: #3a3a3a;
    --muted: #6c7075;
  }
  * { margin: 0; padding: 0; box-sizing: border-box; }
  html, body {
    width: 1200px; height: 1000px; overflow: hidden;
    background: var(--backdrop);
  }
  .canvas {
    position: relative; width: 1200px; height: 1000px;
    display: flex; flex-direction: column; align-items: center; justify-content: center; gap: 60px;
  }
  .card {
    position: relative; width: 700px; height: 400px; overflow: hidden;
    box-shadow: 0 10px 28px rgba(0,0,0,0.22);
  }
  /* Rear side */
  .card-back {
    background: radial-gradient(ellipse at 35% 35%, var(--card-dark-soft), var(--card-dark) 70%);
  }
  .back-brand {
    position: absolute; left: 80px; top: 120px;
    display: flex; align-items: center; gap: 22px;
  }
  .brand-dot {
    width: 44px; height: 44px; border-radius: 50%; background: var(--leaf); flex: none;
  }
  .back-wordmark {
    font-family: "Ubuntu", sans-serif; font-size: 58px; color: var(--wordmark); letter-spacing: 1px;
  }
  .back-rule {
    position: absolute; left: 146px; top: 205px; width: 400px; height: 1px; background: #5d5340;
  }
  .tagline {
    position: absolute; left: 146px; top: 216px;
    font-family: "Ubuntu", sans-serif; font-size: 22px; color: var(--accent); letter-spacing: 1px;
  }
  .back-url {
    position: absolute; left: 80px; bottom: 50px;
    font-family: "Arimo", sans-serif; font-size: 14px; color: var(--muted); letter-spacing: 0.5px;
  }
  /* Front side */
  .card-front { background: var(--card-dark); }
  .front-shape { position: absolute; inset: 0; }
  .front-brand {
    position: absolute; left: 44px; top: 180px; z-index: 1;
    display: flex; align-items: center; gap: 10px;
  }
  .front-brand .brand-dot { width: 22px; height: 22px; }
  .front-wordmark {
    font-family: "Ubuntu", sans-serif; font-size: 24px; line-height: 1; color: var(--wordmark); white-space: nowrap;
  }
  .contact {
    position: absolute; right: 26px; top: 172px; text-align: right;
    font-family: "Arimo", sans-serif; color: var(--ink);
  }
  .person-name { font-size: 27px; color: var(--accent); line-height: 1.1; }
  .person-title { font-size: 20px; margin-top: 6px; color: #444; }
  .address { font-size: 15px; line-height: 1.45; margin-top: 26px; }
  .details { list-style: none; margin-top: 18px; font-size: 12.5px; }
  .details li {
    display: flex; justify-content: flex-end; align-items: center; gap: 14px; height: 24px;
  }
  .details svg { width: 17px; height: 17px; }
</style>
</head>
<body>
<main class="canvas">
  <section class="card card-back" aria-label="Business card rear side">
    <div class="back-brand">
      <span class="brand-dot"></span>
      <span class="back-wordmark">BrambleWorks</span>
    </div>
    <div class="back-rule"></div>
    <p class="tagline">Student Success Platform</p>
    <p class="back-url">www.brambleworks.com.au</p>
  </section>

  <section class="card card-front" aria-label="Business card front side">
    <svg class="front-shape" viewBox="0 0 700 400" width="700" height="400" aria-hidden="true">
      <path d="M158 400 C200 220 380 96 700 82 L700 400 Z" fill="var(--curve-edge)"/>
      <path d="M168 400 C212 226 392 104 700 90 L700 400 Z" fill="var(--card-light)"/>
    </svg>
    <div class="front-brand">
      <span class="brand-dot"></span>
      <span class="front-wordmark">BrambleWorks</span>
    </div>
    <div class="contact">
      <p class="person-name">DANA REYES</p>
      <p class="person-title">Manager</p>
      <p class="address">4120 Fernhill Road<br>Maple Ridge, Lakeview 58213</p>
      <ul class="details">
        <li>12345678909
          <svg viewBox="0 0 24 24" aria-hidden="true"><path d="M6.6 2.5l3 3.2-1.8 2.6c1 2.3 2.9 4.3 5.3 5.5l2.5-1.8 3.3 2.9-1.6 3.1C11 17.8 5.5 12 4.4 5.3z" fill="var(--accent)"/></svg>
        </li>
        <li>hello@brambleworks.com.au
          <svg viewBox="0 0 24 24" aria-hidden="true"><rect x="2" y="5" width="20" height="14" fill="var(--accent)"/><path d="M2 5l10 8 10-8" fill="none" stroke="#fff" stroke-width="1.6"/></svg>
        </li>
        <li>www.brambleworks.com.au
          <svg viewBox="0 0 24 24" aria-hidden="true" fill="none" stroke="var(--accent)" stroke-width="1.6"><circle cx="12" cy="12" r="9.5"/><ellipse cx="12" cy="12" rx="4" ry="9.5"/><path d="M2.5 12h19M4 7h16M4 17h16"/></svg>
        </li>
      </ul>
    </div>
  </section>
</main>
</body>
</html>
```